A Flyer for a clinic/hospital waiting room to warn about patients that they must not abuse our staff

we need a flyer (text attached) with a background of a female nurse or medical doctor photo. I like the example photo where there are four headless satff lined up - something like this, indicating that we are a team and will not tolerate abuse
A4
the text will be over the photo.

Target Market(s)

patients who come to our clinic

Industry/Entity Type

medicine - urology

Colors
0054AA
0677BA
7BADD7
CADEEF
E8F1F8
0094D4
00A9DD
6FCCEA
C7EBF8
E9F6FB

Requirements
Must have
• a photo taking up the whole A4, and text over this. The photos I haev sent are just examples - I will need yo to source a photo
Nice to have
• Horizontal A4 and vertical A4 options. Please add our logo in small , in the bottom right corner

```html
<!DOCTYPE html>
<html lang="en">
<head>
<meta charset="utf-8">
<title>Zero-Tolerance Notice</title>
<link href="https://fonts.googleapis.com/css2?family=Open+Sans:wght@400;600;700;800&display=swap" rel="stylesheet">
<style>
  :root{
    --navy:#1f3a93;
    --panel:rgba(20,40,130,.82);
    --brand-blue:#0054AA;
    --mid-blue:#0677BA;
    --sky:#0094D4;
    --bright:#00A9DD;
    --pale:#C7EBF8;
    --ink:#333333;
    --white:#ffffff;
    --stage:#e9eef3;
  }
  html,body{margin:0;padding:0;width:1200px;height:900px;overflow:hidden;background:var(--stage);font-family:"Open Sans",sans-serif;}
  .poster{position:absolute;left:296px;top:20px;width:608px;height:860px;overflow:hidden;background:var(--sky);}
  .poster-photo{position:absolute;inset:0;width:100%;height:100%;}
  .headline{position:absolute;left:30px;top:18px;width:578px;}
  .headline-row{display:flex;align-items:center;}
  .line-we-have{height:62px;background:var(--navy);width:548px;}
  .we-have{color:var(--white);font-weight:800;font-size:34px;padding:0 14px 0 16px;letter-spacing:.5px;white-space:nowrap;}
  .zero-box{background:var(--white);color:var(--ink);font-weight:800;font-size:38px;padding:0 8px;line-height:52px;letter-spacing:.3px;white-space:nowrap;}
  .line-form{height:66px;background:var(--navy);width:548px;color:var(--white);font-weight:800;font-size:50px;padding-left:16px;box-sizing:border-box;letter-spacing:1px;white-space:nowrap;}
  .line-aggressive{height:70px;background:var(--white);width:548px;color:var(--brand-blue);font-weight:800;font-size:38px;padding-left:14px;box-sizing:border-box;letter-spacing:1px;white-space:nowrap;}
  .notice{position:absolute;left:30px;width:548px;background:var(--panel);color:var(--white);font-weight:600;font-size:14px;line-height:18px;box-sizing:border-box;padding:10px 16px;}
  .notice p{margin:0;text-align:justify;text-align-last:center;}
  .notice p + p{margin-top:14px;}
  .notice-consequence{top:470px;height:94px;}
  .notice-support{top:572px;height:124px;padding-top:16px;}
  .definition{position:absolute;left:30px;top:704px;width:300px;height:156px;background:var(--panel);color:var(--white);box-sizing:border-box;padding:10px 12px;}
  .definition h2{margin:0 0 6px;font-size:14px;line-height:17px;font-weight:800;}
  .definition ul{margin:0;padding:0;list-style:none;font-size:10px;line-height:13px;font-weight:600;}
  .definition li{white-space:nowrap;}
  .definition li::before{content:"\25B8\00a0";}
  .brand-box{position:absolute;left:330px;top:696px;width:248px;height:164px;background:var(--white);display:flex;flex-direction:column;align-items:center;justify-content:center;gap:10px;}
  .brand-dot{width:46px;height:46px;border-radius:50%;background:var(--bright);}
  .brand-name{color:var(--brand-blue);font-weight:600;font-size:22px;}
</style>
</head>
<body>
  <main class="poster">
    <svg class="poster-photo" viewBox="0 0 608 860" preserveAspectRatio="none" role="img" aria-label="Photo of medical staff in scrubs and white coats with stethoscopes standing side by side with arms crossed, tinted blue">
      <defs>
        <linearGradient id="photoTone" x1="0" y1="0" x2="1" y2="1">
          <stop offset="0" stop-color="#0677BA"/>
          <stop offset=".45" stop-color="#00A9DD"/>
          <stop offset=".75" stop-color="#0094D4"/>
          <stop offset="1" stop-color="#0054AA"/>
        </linearGradient>
      </defs>
      <rect width="608" height="860" fill="url(#photoTone)"/>
    </svg>

    <header class="headline">
      <div class="headline-row line-we-have">
        <span class="we-have">WE HAVE</span>
        <span class="zero-box">ZERO-TOLERANCE</span>
      </div>
      <div class="headline-row line-form">FOR ANY FORM OF</div>
      <div class="headline-row line-aggressive">AGGRESSIVE BEHAVIOUR</div>
    </header>

    <section class="notice notice-consequence">
      <p>If any of our staff feel intimidated in any way, we will always support them. Incidents will result in your immediate removal from the facility, termination of your relationship with the practice, and may result in prosecution.</p>
    </section>

    <section class="notice notice-support">
      <p>In all circumstances we will support any staff member who wishes to press charges against a perpetrator of aggressive behaviour.</p>
      <p>We take this stance because our staff work extremely hard in busy circumstances to help you and we will no longer tolerate any form of aggression or abuse.</p>
    </section>

    <section class="definition">
      <h2>Aggressive behaviour (in-person or on the telephone) is:</h2>
      <ul>
        <li>Verbal harassment</li>
        <li>Any verbal or physical confrontation</li>
        <li>Raising your voice or making unreasonable demands</li>
        <li>Abusive or intimidating behaviour</li>
        <li>Sexual or suggestive language or behaviour</li>
        <li>Making threats to our staff</li>
        <li>Swearing</li>
      </ul>
    </section>

    <aside class="brand-box">
      <span class="brand-dot"></span>
      <span class="brand-name">Riverbend Urology</span>
    </aside>
  </main>
</body>
</html>
```